New Architectural Firm Business Cards

New Business card to compliment previous pixel forum logo (attached). Please design a business card that is simple, modern, creative....please do not use "symbols", simply the logo and associated graphics/text. The front should contain name/address/phone/email/web address (with graphics).....back should be 100% graphic design using the logo somehow. Hoping for a two color (black and yellow) design. full bleed design, no borders

Target Market(s)

Commercial Architecture Clients

Industry/Entity Type

Architecture

Contact Information for Business Card

Please design a business card that is simple, modern, creative....please do not use "symbols", simply the logo and associated graphics/text. The front should contain name/address/phone/email/web address (with graphics).....back should be 100% graphic design using the logo somehow

Font styles to use
Sans Serif

Colors
FFF300
FFF600
FEFA6F
FFFEC7
FFFEE8

Requirements
Must have
• Clean, Modern Design
Should not have
• Stock images or "icons"

```html
<!DOCTYPE html>
<html lang="en">
<head>
<meta charset="utf-8">
<title>Kestrel Architecture – Business Card</title>
<link rel="stylesheet" href="https://fonts.googleapis.com/css2?family=Lato:wght@400;700;900&family=Libre+Baskerville:wght@700&display=swap">
<style>
  :root {
    --yellow: #f7c413;
    --ink: #2b2a29;
    --black: #111111;
    --paper: #ffffff;
    --backdrop: #d7d7d7;
  }
  * { margin: 0; padding: 0; box-sizing: border-box; }
  html, body { width: 1200px; height: 1000px; overflow: hidden; }
  body {
    position: relative;
    background: var(--backdrop);
    font-family: "Lato", Arial, sans-serif;
    color: var(--ink);
  }
  .card {
    position: absolute;
    left: 258px;
    width: 687px;
    height: 383px;
  }
  .card--front { top: 82px; background: var(--yellow); }
  .card--back { top: 530px; background: var(--paper); }

  .holder { position: absolute; left: 62px; top: 42px; }
  .holder__name {
    font-family: "Libre Baskerville", Georgia, serif;
    font-weight: 700;
    font-size: 34px;
    color: var(--black);
    letter-spacing: 0.2px;
  }
  .holder__role {
    margin-top: 4px;
    text-align: right;
    font-size: 19px;
    letter-spacing: 1.6px;
    color: var(--black);
  }

  .contact-list {
    position: absolute;
    right: 193px;
    top: 208px;
    list-style: none;
  }
  .contact-list__item {
    display: flex;
    justify-content: flex-end;
    align-items: center;
    height: 35.5px;
    font-size: 19px;
    letter-spacing: 2.2px;
    color: var(--black);
  }
  .contact-list__icon {
    width: 29px;
    height: 23px;
    margin-left: 11px;
    border-radius: 6px;
    background: var(--ink);
    display: flex;
    align-items: center;
    justify-content: center;
  }
  .contact-list__icon svg { width: 15px; height: 15px; }

  .brand-mark {
    position: absolute;
    border-radius: 50%;
    display: flex;
    align-items: center;
    justify-content: center;
    text-align: center;
    font-family: "Lato", Arial, sans-serif;
    font-weight: 900;
    text-transform: uppercase;
    line-height: 1.15;
  }
  .brand-mark--small {
    left: 506px;
    top: 211px;
    width: 134px;
    height: 130px;
    background: var(--ink);
    color: var(--yellow);
    font-size: 13px;
    letter-spacing: 0.5px;
  }
  .brand-mark--large {
    left: 191px;
    top: 43px;
    width: 310px;
    height: 298px;
    background: var(--yellow);
    color: var(--ink);
    font-size: 30px;
    letter-spacing: 1px;
  }
</style>
</head>
<body>

<section class="card card--front" aria-label="Business card front">
  <div class="holder">
    <h1 class="holder__name">Alex Reyes</h1>
    <p class="holder__role">Senior Architect</p>
  </div>

  <ul class="contact-list">
    <li class="contact-list__item">+00 21 468 3097
      <span class="contact-list__icon">
        <svg viewBox="0 0 16 16"><path fill="#fff" d="M4 1.5l2.2 3-1.3 1.5c.8 1.9 2.3 3.4 4.2 4.2l1.5-1.3 3 2.2-1 2.5C7.300 13.600 2.400 8.700 1.500 3z"/></svg>
      </span>
    </li>
    <li class="contact-list__item">www.kestrelarch.com
      <span class="contact-list__icon">
        <svg viewBox="0 0 16 16"><rect x="1.5" y="2" width="13" height="9" rx="1" fill="none" stroke="#fff" stroke-width="1.6"/><rect x="6" y="11.5" width="4" height="2" fill="#fff"/><rect x="4" y="13.3" width="8" height="1.4" fill="#fff"/></svg>
      </span>
    </li>
    <li class="contact-list__item">info@kestrelarch.com
      <span class="contact-list__icon">
        <svg viewBox="0 0 16 16"><rect x="1" y="3" width="14" height="10" rx="1" fill="#fff"/><path d="M1.5 3.8L8 9l6.5-5.2" fill="none" stroke="#2b2a29" stroke-width="1.3"/></svg>
      </span>
    </li>
    <li class="contact-list__item">45 Harbour Lane
      <span class="contact-list__icon">
        <svg viewBox="0 0 16 16"><path fill="#fff" d="M8 1a4.5 4.5 0 0 0-4.5 4.5C3.500 9 8 15 8 15s4.500-6 4.500-9.500A4.500 4.500 0 0 0 8 1zm0 6.3a1.800 1.800 0 1 1 0-3.600 1.800 1.800 0 0 1 0 3.600z"/></svg>
      </span>
    </li>
  </ul>

  <div class="brand-mark brand-mark--small">Kestrel<br>Architecture</div>
</section>

<section class="card card--back" aria-label="Business card back">
  <div class="brand-mark brand-mark--large">Kestrel<br>Architecture</div>
</section>

</body>
</html>
```